IT consulting company looking for a modern business design for a website and a new logo

We are the IT-consulting company VendiMark from Germany and need a new and modern business website and a new logo. We are specialized in output management. Our services include business analysis, outsourcing, development, training and project leading. We wish for a design with nature pictures (mountains, lakes, rivers, forests, etc.) for our company with the colors green and blue. If it is possible, a slow-mo video of a nature scene. The design should be responsive and the menu should change to a hamburger menu. The following are: • Services / Solutions 1. Output Management 2. Outsourcing 3. Development 4. Business Analyst 5. Training • Partners • Careers • About Us 1. Project A 2. Project B 3. Project C • Contact Notes for the following categories: For "Services / Solutions" we want to conclude some contents from all the sub-points and sub-points below. Additionally, we would like to see some sub-point under "Services / Solutions". For Output Management: "5 Benefits of Output Management Systems (OMS) - OMS Simplifies and Accelerates External Communication - Helps Reduce Communication Mistakes - Provides Customers With Fast and Secure Responses to your questions - Employees can focus on the essential as they can access prepared templates - Companies get complete transparency about their communication "The point" partner does not have sub-points. The content here is a quote and the logo from the company Brel. For now, just placeholders on this site. The next point wants to be "career" without sub-point and wants to contain some text. Carrer options wants to be listed here. Next point wants to be "About us", where we need sub-points which we do not know exactly at this moment, but they will contain text. By clicking directly on "About us" we want to include pictures and texts about 6 employees for which we only need placeholders at the moment. The last point wants to be "contact", where customers can send us messages. The main page should include a story about our company, which can be a placeholder for now. For reference, designs have a look at: https://brelvantix.de/ https://www.lumortika.com/ https://www.tpvrano.de/ We prefer WordPress designs, created with the plugin ELEMENTOR, so that we can easily edit the content by ourselves. The final design should look professional, competent and modern.

Target Market(s)

With our website, we want to reach the following target groups. <br> <br> <br> <br> <br> <br> <br> <br> <br> <br> <br> <br> <br> <br> <br> <br> <br> <br> <br> <br> <br> <br> <br> <br> <br> <br> <br> <br> <br> <br> <br> <br> <br> <br> <br> <br> <br> <br> <br> <br> <br> <br> <br> <br> <br> <br> <br> <br> <br>

Industry/Entity Type

Consulting

Logo Text

(optionally) VendiMark

Font styles to use
Sans Serif

Colors

Designer to choose colors to be used in the design.

Requirements
Must have
• 1. Outsourcing 3. Development 4. Business Analyst 5. Training • Partners • Careers • About Us 1. Project A 2. Project B 3. Project C • Contact The above-mentioned background picture with nature motifs (mountains, lakes, rivers, forests, etc.). WordPress design in primary colors blue and green.
Nice to have
• ELEMENTOR template. Effects for the background pictures. Counter of all successful projects for Output Management, Business Analyst and Training

```html
<!DOCTYPE html>
<html lang="en">
<head>
<meta charset="utf-8">
<title>VendiMark – IT Consulting</title>
<link href="https://fonts.googleapis.com/css2?family=Poppins:wght@400;500;600;700&family=Open+Sans:wght@400;600&display=swap" rel="stylesheet">
<style>
:root{
  --green:#17a98b;
  --green-dark:#12937a;
  --ink:#1e1e1e;
  --text:#6f6f6f;
  --muted:#8a8a8a;
  --line:#e6e6e6;
  --light:#f6f7f7;
  --footer:#2a2a2a;
  --footer-bottom:#1f1f1f;
  --white:#ffffff;
}
*{box-sizing:border-box;margin:0;padding:0}
html,body{width:1200px;height:3600px;overflow:hidden}
body{font-family:"Open Sans",Arial,sans-serif;color:var(--text);background:var(--white);position:relative;font-size:13px;line-height:1.6}
h1,h2,h3,h4,.btn,.nav,.logo{font-family:"Poppins",Arial,sans-serif}
.btn{display:inline-block;background:var(--green);color:var(--white);font-size:11px;font-weight:600;text-transform:uppercase;letter-spacing:.5px;border-radius:22px;padding:0 26px;height:38px;line-height:38px}
.btn-white{background:var(--white);color:var(--ink)}
.heading-bar{border-left:4px solid var(--green);padding-left:16px;color:var(--ink);font-weight:600}

/* top bar */
.topbar{position:absolute;top:0;left:0;width:1200px;height:39px;background:var(--green);color:var(--white);font-size:11px;display:flex;align-items:center;padding:0 174px 0 270px;justify-content:space-between}
.topbar .contacts{display:flex;gap:30px}
.topbar .contacts span{display:flex;align-items:center;gap:7px}
.social{display:flex;gap:12px}
.social i{display:block;width:9px;height:9px;border-radius:50%;background:currentColor}
/* nav */
.navbar{position:absolute;top:39px;left:0;width:1200px;height:66px;display:flex;align-items:center;padding:0 160px 0 174px;justify-content:space-between}
.logo{display:flex;align-items:center;gap:8px;font-size:28px;font-weight:500;color:#2b3540}
.logo i{width:22px;height:22px;border-radius:50%;background:#1f7fb6;display:block}
.nav{display:flex;gap:26px;font-size:11px;font-weight:500;text-transform:uppercase;color:#333;align-items:center}
.nav .search{margin-left:40px}
/* hero */
.hero{position:absolute;top:105px;left:0;width:1200px;height:420px;background:linear-gradient(180deg,#8fb3cf 0%,#b8cde0 35%,#e7eef4 62%,#7d8ea0 100%);text-align:center}
.hero h1{margin-top:100px;font-size:37px;font-weight:400;color:var(--white);letter-spacing:.5px}
.hero .btn{margin-top:30px;padding:0 42px;height:46px;line-height:46px}
/* feature cards */
.features{position:absolute;top:480px;left:159px;width:885px;height:285px;display:flex;gap:6px}
.feature{flex:1;background:var(--white);box-shadow:0 3px 14px rgba(0,0,0,.12);padding:34px 24px}
.feature svg{width:52px;height:52px;stroke:#2d5d9f;fill:none;stroke-width:2}
.feature h3{margin-top:24px;font-size:15px;font-weight:600;color:var(--ink);line-height:1.35}
.feature p{margin-top:10px;font-size:11.5px;line-height:1.55}
/* solution */
.solution{position:absolute;top:831px;left:171px;width:873px;height:309px;display:flex;gap:48px}
.media{width:408px;height:309px;background:linear-gradient(135deg,#8d9aa8,#c9c2b8 55%,#5c6672);position:relative}
.play{position:absolute;left:186px;top:135px;width:44px;height:32px;background:#d92b2b;border-radius:7px}
.play:after{content:"";position:absolute;left:17px;top:9px;border-left:12px solid #fff;border-top:7px solid transparent;border-bottom:7px solid transparent}
.solution .body{padding-top:54px;width:400px}
.solution h2{font-size:25px}
.solution p{margin-top:28px;font-size:11.5px;line-height:1.65}
.solution .btn{margin-top:26px}
/* stats */
.stats{position:absolute;top:1209px;left:0;width:1200px;height:201px;background:var(--light);display:flex;padding:60px 0 0 165px;gap:0}
.stat{display:flex;gap:22px;width:290px}
.stat svg{width:52px;height:52px;stroke:#2d5d9f;fill:none;stroke-width:2}
.stat b{font-family:"Poppins",sans-serif;font-size:34px;font-weight:600;color:var(--ink);display:block;line-height:1}
.stat small{display:block;font-size:12px;line-height:1.4;margin-top:6px;color:var(--ink)}
.stat small em{font-style:normal;color:var(--green)}
/* ready */
.ready{position:absolute;top:1470px;left:171px;width:420px}
.ready h2{font-size:24px;line-height:1.3}
.ready p{font-size:11px;margin-top:20px;line-height:1.7}
.ready ul{list-style:none;margin-top:14px;font-size:11px}
.ready li{display:flex;align-items:center;gap:10px;line-height:2}
.ready li svg{width:12px;height:12px;stroke:var(--green);fill:none;stroke-width:2.5}
.help{position:absolute;top:1500px;left:600px;width:435px;height:315px;background:var(--green);padding:62px 0 0 24px;color:var(--white)}
.help h3{border-left:4px solid var(--white);padding-left:14px;font-size:24px;font-weight:600;line-height:1.25}
.help p{font-size:11px;margin-top:14px;width:250px;line-height:1.6}
.help .btn{margin-top:22px}
.person{position:absolute;top:1455px;left:855px;width:225px;height:360px;background:linear-gradient(180deg,#dfe3e6,#3f4a58 45%,#2c3440);border-radius:110px 110px 0 0}
/* strategy band */
.band{position:absolute;top:1875px;left:0;width:1200px;height:225px;background:linear-gradient(90deg,#17a98b,#2cb99a 50%,#17a98b);}
.band h2{position:absolute;left:171px;top:66px;font-size:20px;font-weight:600;color:var(--white);line-height:1.5;text-transform:uppercase;width:600px}
.band .btn{position:absolute;left:849px;top:75px;height:40px;line-height:40px}
/* services */
.services{position:absolute;top:2025px;left:159px;width:885px;height:705px;background:var(--white);box-shadow:0 3px 16px rgba(0,0,0,.1);text-align:center}
.services h2{margin-top:36px;font-size:28px;font-weight:600;color:var(--ink)}
.services .intro{width:640px;margin:14px auto 0;font-size:11.5px;line-height:1.6}
.grid{position:absolute;top:180px;left:0;width:885px;display:grid;grid-template-columns:1fr 1fr;text-align:left}
.tile{height:261px;display:flex}
.tile .ph{width:216px;height:261px}
.tile .txt{width:226px;padding:46px 24px}
.tile h3{font-size:17px;font-weight:600;color:var(--ink);line-height:1.3}
.tile p{font-size:11px;margin-top:12px;line-height:1.6}
.tile .btn{margin-top:16px;height:34px;line-height:34px;padding:0 22px}
.ph-a{background:linear-gradient(135deg,#34506f,#a9bfd3 60%,#e5e9ee)}
.ph-b{background:linear-gradient(135deg,#eef0f2,#c8b7a4 50%,#8b99a8)}
.ph-c{background:linear-gradient(135deg,#2d3a48,#c9ced4 60%,#f0f1f3)}
.ph-d{background:linear-gradient(135deg,#dfe4e8,#a7b2bd 55%,#6a7786)}
/* partners */
.partners{position:absolute;top:2820px;left:171px;width:420px}
.partners h2{font-size:27px}
.partners p{margin-top:30px;font-size:11.5px;line-height:1.6}
.partners .btn{margin-top:24px}
.badges{position:absolute;top:2830px;left:600px;width:430px;display:grid;grid-template-columns:repeat(3,120px);gap:28px 20px}
.badge{height:60px;border-radius:4px}
.pager{position:absolute;top:3030px;left:780px;display:flex;gap:10px}
.pager span{width:36px;height:36px;background:var(--green);display:flex;align-items:center;justify-content:center}
.pager svg{width:12px;height:12px;stroke:#fff;stroke-width:2.5;fill:none}
/* footer */
.footer{position:absolute;top:3126px;left:0;width:1200px;height:414px;background:var(--footer);color:#cfcfcf}
.col{position:absolute;top:60px}
.col h4{color:var(--white);font-size:17px;font-weight:600;border-left:3px solid var(--green);padding-left:12px}
.col1{left:171px;width:250px}
.col2{left:465px;width:265px}
.col3{left:756px;width:270px}
.info{margin-top:34px;font-size:11px;list-style:none}
.info li{display:flex;gap:14px;margin-bottom:16px;line-height:1.6}
.info svg{flex:none;width:12px;height:12px;fill:#cfcfcf;margin-top:3px}
.col1 .social{margin-left:24px;color:#cfcfcf}
.field{height:38px;background:#444;margin-top:8px;font-size:11px;color:#999;padding:10px 12px}
.col2 form{margin-top:30px}
.field.big{height:98px}
.submit{margin-top:14px;height:28px;background:var(--green);color:#fff;font-family:"Poppins",sans-serif;font-size:11px;font-weight:600;text-align:center;line-height:28px}
.col3 p{margin-top:30px;font-size:11px;line-height:1.6}
.col3 .field{background:#e9e9e9;height:36px;margin-top:14px}
.footbar{position:absolute;top:3540px;left:0;width:1200px;height:60px;background:var(--footer-bottom);color:#aaa;font-size:11px;padding:20px 171px}
.footbar em{font-style:normal;color:var(--green)}
.totop{position:absolute;top:3555px;left:984px;width:30px;height:30px;background:#4d7ab8;display:flex;align-items:center;justify-content:center}
.totop svg{width:12px;height:12px;stroke:#fff;stroke-width:2.5;fill:none}
</style>
</head>
<body>

<div class="topbar">
  <div class="contacts"><span>☎ 000 - 0000 - 0000</span><span>✉ info@vendimark.com</span></div>
  <div class="social"><i></i><i></i><i></i></div>
</div>

<header class="navbar">
  <div class="logo"><i></i>VendiMark</div>
  <nav class="nav"><span>Home</span><span>Services ▾</span><span>Partner</span><span>Career</span><span>About Us ▾</span><span>Contact</span>
    <svg class="search" width="13" height="13" viewBox="0 0 14 14" fill="none" stroke="#333" stroke-width="2"><circle cx="6" cy="6" r="4.5"/><path d="M9.5 9.5L13 13"/></svg>
  </nav>
</header>

<section class="hero" role="img" aria-label="Snow-covered mountain range under a pale blue sky">
  <h1>We Help Your Business to Grow</h1>
  <span class="btn">Ask for consultation</span>
</section>

<section class="features">
  <div class="feature">
    <svg viewBox="0 0 52 52"><rect x="6" y="22" width="18" height="24"/><rect x="24" y="12" width="20" height="34"/><path d="M10 28h4M10 34h4M30 18h4M30 24h4M30 30h4M2 46h48"/></svg>
    <h3>Energy<br>Companies</h3>
    <p>Duis aute irure dolor in velit esse cillum dolore eu fugiat nulla pariatur.</p>
  </div>
  <div class="feature">
    <svg viewBox="0 0 52 52"><path d="M26 6l16 6v12c0 11-7 18-16 22-9-4-16-11-16-22V12z"/><path d="M19 26l5 5 9-10"/></svg>
    <h3>Insurance<br>Companies</h3>
    <p>Duis aute irure dolor in velit esse cillum dolore eu fugiat nulla pariatur.</p>
  </div>
  <div class="feature">
    <svg viewBox="0 0 52 52"><circle cx="26" cy="12" r="7"/><circle cx="14" cy="32" r="7"/><circle cx="38" cy="32" r="7"/><path d="M6 46h40"/></svg>
    <h3>Financial<br>Corporations</h3>
    <p>Duis aute irure dolor in velit esse cillum dolore eu fugiat nulla pariatur.</p>
  </div>
  <div class="feature">
    <svg viewBox="0 0 52 52"><rect x="6" y="18" width="10" height="28"/><rect x="20" y="8" width="12" height="38"/><rect x="36" y="14" width="10" height="32"/><path d="M2 46h48"/></svg>
    <h3>Large<br>Enterprises</h3>
    <p>Duis aute irure dolor in velit esse cillum dolore eu fugiat nulla pariatur.</p>
  </div>
</section>

<section class="solution">
  <div class="media" role="img" aria-label="Video still of a business team meeting around a table"><span class="play"></span></div>
  <div class="body">
    <h2 class="heading-bar">Meet Our New Solution</h2>
    <p>Nemo enim ipsam voluptatem quia voluptas sit aspernatur aut odit aut fugit, sed quia consequuntur magni dolores eos qui ratione voluptatem sequi nesciunt. Neque porro quisquam est, qui dolorem ipsum quia dolor sit amet.</p>
    <span class="btn">Read more</span>
  </div>
</section>

<section class="stats">
  <div class="stat">
    <svg viewBox="0 0 52 52"><path d="M16 8h20v12a10 10 0 0 1-20 0z"/><path d="M16 12H8c0 8 4 12 9 12M36 12h8c0 8-4 12-9 12M26 30v8M18 44h16v-6H18z"/></svg>
    <div><b>250+</b><small><em>Successfully</em><br>Completed Projects</small></div>
  </div>
  <div class="stat">
    <svg viewBox="0 0 52 52"><circle cx="26" cy="26" r="20"/><path d="M6 26h40M26 6c-8 8-8 32 0 40M26 6c8 8 8 32 0 40"/></svg>
    <div><b>400+</b><small><em>Happy Clients</em><br>Around the World</small></div>
  </div>
  <div class="stat">
    <svg viewBox="0 0 52 52"><circle cx="26" cy="29" r="18"/><path d="M26 29V18M21 5h10M26 5v6M40 14l4-4"/></svg>
    <div><b>10</b><small><em>Years</em><br>Of Experience</small></div>
  </div>
</section>

<section class="ready">
  <h2 class="heading-bar">We Are Always Ready<br>For You</h2>
  <p>Quis autem vel eum iure reprehenderit qui in ea voluptate velit esse quam nihil molestiae consequatur, vel illum qui dolorem eum fugiat quo voluptas nulla pariatur. Duis aute irure dolor in reprehenderit in voluptate velit esse.</p>
  <ul>
    <li><svg viewBox="0 0 12 12"><path d="M1 6l3 3 7-7"/></svg>Excepteur sint occaecat cupidatat non proident</li>
    <li><svg viewBox="0 0 12 12"><path d="M1 6l3 3 7-7"/></svg>Nemo enim ipsam voluptatem quia voluptas sit aspernatur</li>
    <li><svg viewBox="0 0 12 12"><path d="M1 6l3 3 7-7"/></svg>Quis autem vel eum iure reprehenderit qui in ea voluptate</li>
  </ul>
  <p>Quis autem vel eum iure reprehenderit qui in ea voluptate velit esse quam nihil molestiae consequatur, vel illum qui dolorem eum fugiat quo voluptas nulla pariatur. Duis aute irure dolor in reprehenderit in voluptate velit esse.</p>
</section>
<div class="help">
  <h3>Helping Your<br>Business</h3>
  <p>Nemo enim ipsam voluptatem quia voluptas sit aspernatur aut odit aut fugit, sed quia consequuntur magni dolores eos qui ratione voluptatem sequi nesciunt.</p>
  <span class="btn btn-white">Read more</span>
</div>
<div class="person" role="img" aria-label="Smiling consultant in a suit with arms crossed"></div>

<section class="band" role="img" aria-label="Green-tinted photo of a business team at work">
  <h2>We help you to make the best marketable<br>strategy, asset and execution</h2>
  <span class="btn btn-white">Our responsibility</span>
</section>

<section class="services">
  <h2>Our Services</h2>
  <p class="intro">Quis autem vel eum iure reprehenderit qui in ea voluptate velit esse quam nihil molestiae consequatur vel illum qui dolorem eum fugiat quo voluptas nulla pariatur.</p>
  <div class="grid">
    <div class="tile"><div class="ph ph-a" role="img" aria-label="Hands holding a tablet showing analysis charts"></div><div class="txt"><h3>Business<br>Analysis</h3><p>Quis nostrum exercitationem ullam corporis suscipit hic et dolore.</p><span class="btn">Read more</span></div></div>
    <div class="tile"><div class="ph ph-b" role="img" aria-label="Two colleagues working together at a laptop"></div><div class="txt"><h3>Business<br>Outsourcing</h3><p>Quis nostrum exercitationem ullam corporis suscipit hic et dolore.</p><span class="btn">Read more</span></div></div>
    <div class="tile"><div class="txt"><h3>Business<br>Development</h3><p>Quis nostrum exercitationem ullam corporis suscipit hic et dolore.</p><span class="btn">Read more</span></div><div class="ph ph-c" role="img" aria-label="Business handshake close-up"></div></div>
    <div class="tile"><div class="txt"><h3>Business Trainings<br>&amp; Project Leading</h3><p>Quis nostrum exercitationem ullam corporis suscipit hic et dolore.</p><span class="btn">Read more</span></div><div class="ph ph-d" role="img" aria-label="Trainer presenting at a whiteboard to a team"></div></div>
  </div>
</section>

<section class="partners">
  <h2 class="heading-bar">Our Partners</h2>
  <p>Quis autem vel eum iure reprehenderit qui in ea voluptate velit esse quam nihil molestiae consequatur, vel illum qui dolorem eum fugiat quo voluptas nulla pariatur.</p>
  <span class="btn">Read more</span>
</section>
<div class="badges">
  <div class="badge" style="background:#c8452f"></div>
  <div class="badge" style="background:#2f6fb0"></div>
  <div class="badge" style="background:#1f3f6b"></div>
  <div class="badge" style="background:#284a7a"></div>
  <div class="badge" style="background:#2a62a8"></div>
</div>
<div class="pager">
  <span><svg viewBox="0 0 12 12"><path d="M8 1L3 6l5 5"/></svg></span>
  <span><svg viewBox="0 0 12 12"><path d="M4 1l5 5-5 5"/></svg></span>
</div>

<footer class="footer">
  <div class="col col1">
    <h4>Contact Us</h4>
    <ul class="info">
      <li><svg viewBox="0 0 12 12"><path d="M6 0a4 4 0 0 0-4 4c0 3 4 8 4 8s4-5 4-8a4 4 0 0 0-4-4zm0 5.5A1.5 1.5 0 1 1 6 2.5a1.5 1.5 0 0 1 0 3z"/></svg>124A, sed quia non numquam eius modi tempora incidunt ut labore</li>
      <li><svg viewBox="0 0 12 12"><path d="M2 1l2-1 2 3-1.5 1.5a7 7 0 0 0 3 3L9 6l3 2-1 2C6 11 1 6 2 1z"/></svg>000 - 0000 - 0000</li>
      <li><svg viewBox="0 0 12 12"><path d="M0 2h12v8H0zM0 2l6 4 6-4" /></svg>info@vendimark.com</li>
    </ul>
    <div class="social"><i></i><i></i><i></i></div>
  </div>
  <div class="col col2">
    <h4>Quick Contact</h4>
    <form>
      <div class="field">Name...</div>
      <div class="field">Email...</div>
      <div class="field big">Message...</div>
      <div class="submit">SUBMIT</div>
    </form>
  </div>
  <div class="col col3">
    <h4>Newsletter</h4>
    <p>Subscribe to our newsletter for latest updates</p>
    <div class="field">Email...</div>
    <div class="submit">SUBSCRIBE</div>
  </div>
</footer>
<div class="footbar">©Copyright Information here | Designed by <em>Studio North</em></div>
<div class="totop"><svg viewBox="0 0 12 12"><path d="M1 8l5-5 5 5"/></svg></div>

</body>
</html>
```